Simple elegant feminine design - Going out on my own as a Mortgage Broker.
My thoughts are the following details on the Front, middle of the card possibly? Phone and email smaller font than my name?
Marnie Veltrin
Finance Specialist
p: 0438 215 962
e: marnie@veltrinlending.com.au
Bottom of the card
residential / commercial / equipment
I would like the Font in Rose Gold maybe white or black background? or Possibly a stone grey - are you able to do a few options? I'd like them embossed
Then I had an idea as a simple logo as per the attached if you get the idea in my scribble, my initials, capital M attached to a small v that leads/follows into a circle? Thicker Font In Rose Gold, middle of the card at the back.
Very open to ideas though and what colour you think would look better with the Rose Gold.
Thanks so much for your help, I am not very creative and savvy with this stuff :-)
Industry/Entity Type
Finance
Contact Information for Business Card
Marnie Veltrin
p: 0438 215 962
Look and feel

```html
<!DOCTYPE html>
<html lang="en">
<head>
<meta charset="utf-8">
<title>Marnie Veltrin – Finance Specialist</title>
<link rel="stylesheet" href="https://fonts.googleapis.com/css2?family=Caladea&display=swap">
<style>
  :root {
    --card-base: #2f2e2d;
    --card-light: #363534;
    --card-dark: #262524;
    --rose-light: #f2c9a8;
    --rose-mid: #d8976f;
    --rose-deep: #a8613f;
    --emboss-shadow: rgba(0, 0, 0, 0.75);
    --emboss-light: rgba(255, 235, 220, 0.18);
  }
  html, body {
    margin: 0;
    padding: 0;
    width: 1200px;
    height: 756px;
    overflow: hidden;
    background: var(--card-dark);
  }
  .card {
    position: relative;
    width: 1200px;
    height: 756px;
    box-sizing: border-box;
    border: 2px solid #1c1b1a;
    background:
      radial-gradient(ellipse at 50% 40%, var(--card-light) 0%, var(--card-base) 55%, var(--card-dark) 100%);
    font-family: "Caladea", "Cambria", Georgia, serif;
  }
  .rose-gold {
    background: linear-gradient(180deg, var(--rose-light) 0%, var(--rose-mid) 50%, var(--rose-deep) 100%);
    -webkit-background-clip: text;
    background-clip: text;
    color: transparent;
    filter: drop-shadow(2px 3px 2px var(--emboss-shadow)) drop-shadow(-1px -1px 0 var(--emboss-light));
    white-space: nowrap;
    margin: 0;
    line-height: 1;
    position: absolute;
  }
  .name {
    left: 362px;
    top: 206px;
    font-size: 71px;
    font-weight: 400;
  }
  .title {
    left: 363px;
    top: 286px;
    font-size: 42px;
  }
  .contact-phone {
    left: 363px;
    top: 417px;
    font-size: 28px;
  }
  .contact-email {
    left: 363px;
    top: 450px;
    font-size: 28px;
  }
  .services {
    left: 142px;
    top: 644px;
    font-size: 51px;
  }
</style>
</head>
<body>
  <main class="card">
    <h1 class="rose-gold name">Marnie Veltrin</h1>
    <p class="rose-gold title">Finance Specialist</p>
    <p class="rose-gold contact-phone">0438215962</p>
    <p class="rose-gold contact-email">marnie@veltrinlending.com.au</p>
    <p class="rose-gold services">Residential / Commercial / Equipment</p>
  </main>
</body>
</html>
```